Brightwell Essence colloidal silver spray for pets.

We need a label for an 8-oz cobalt blue spray bottle. We are a small company just starting to share the benefits of colloidal silver. Our first offering will be the 8-oz spray bottle for pets. We would also like to update our logo. The finished project should be crisp and incorporate a dog on the label. I have attached the information we would like on the label and our logo, which can be changed to match your vision.
Updates

Hi, I would like to remind you that we are using a cobalt blue bottle with a black sprayer and would like an updated logo. Also, for the business cards, we don't want an animal on them, as we are planning future products for people. thank you

```html
<!DOCTYPE html>
<html lang="en">
<head>
<meta charset="utf-8">
<title>Brightwell Essence – Colloidal Silver Pet Spray Label</title>
<link rel="stylesheet" href="https://fonts.googleapis.com/css2?family=Stint+Ultra+Condensed&family=Cabin:wght@500;600;700&display=swap">
<style>
  :root {
    --bg: #ececec;
    --ink-dark: #3a3a3c;
    --label-top: #dcdff3;
    --label-mid: #a9b0dc;
    --label-fur: #4a6478;
    --title-green: #0f8a45;
    --pill-navy: #2e2f8c;
    --white: #ffffff;
    --flag-red: #e0202a;
  }
  * { margin: 0; padding: 0; box-sizing: border-box; }
  html, body { width: 1200px; height: 1200px; overflow: hidden; }
  body {
    background: radial-gradient(circle at 50% 50%, #fafafa 0%, var(--bg) 70%, #dcdcdc 100%);
    font-family: "Cabin", sans-serif;
    position: relative;
  }

  /* Brand lockup */
  .brand-lockup {
    position: absolute;
    left: 60px; top: 520px;
    width: 500px;
    text-align: center;
  }
  .brand-lockup__name {
    font-weight: 700;
    font-size: 58px;
    color: var(--ink-dark);
    letter-spacing: 1px;
    line-height: 1.1;
    white-space: nowrap;
  }
  .brand-lockup__rule {
    margin: 18px auto 0;
    width: 320px;
    height: 6px;
    background: var(--ink-dark);
  }

  /* Label */
  .label {
    position: absolute;
    left: 650px; top: 100px;
    width: 478px; height: 1002px;
    overflow: hidden;
    background: linear-gradient(180deg, var(--label-top) 0%, #c4c8ea 25%, var(--label-mid) 42%, #7f8fb4 52%, var(--label-fur) 64%, #3d5568 100%);
  }
  .label__photo {
    position: absolute;
    left: 0; top: 560px;
    width: 478px; height: 442px;
    background: radial-gradient(ellipse at 45% 45%, #e2c08c 0%, #c99e63 30%, rgba(90,110,130,0.6) 62%, rgba(60,85,104,0) 80%);
  }
  .label__banner {
    position: absolute;
    left: 144px; top: 0;
    width: 188px; height: 106px;
  }
  .label__banner-name {
    position: absolute;
    left: 144px; top: 20px;
    width: 188px;
    text-align: center;
    font-weight: 700;
    font-size: 22px;
    line-height: 1.1;
    color: var(--ink-dark);
  }
  .label__title {
    position: absolute;
    left: 0; top: 112px;
    width: 478px;
    text-align: center;
    font-family: "Stint Ultra Condensed", serif;
    font-weight: 400;
    color: var(--title-green);
    font-size: 124px;
    line-height: 104px;
    letter-spacing: 0;
    text-transform: uppercase;
    white-space: nowrap;
  }
  .label__pill {
    position: absolute;
    left: 46px; top: 343px;
    width: 384px; height: 78px;
    border-radius: 14px;
    background: var(--pill-navy);
    color: var(--white);
    font-weight: 700;
    font-size: 29px;
    line-height: 36px;
    text-align: center;
    padding-top: 4px;
    letter-spacing: 1px;
  }
  .label__specs {
    position: absolute;
    left: 0; top: 436px;
    width: 478px;
    text-align: center;
    color: var(--white);
    font-weight: 600;
    font-size: 20px;
    line-height: 23px;
  }
  .label__rule {
    position: absolute;
    left: 128px; top: 492px;
    width: 222px; height: 2px;
    background: var(--white);
  }
  .label__claims {
    position: absolute;
    left: 0; top: 502px;
    width: 478px;
    text-align: center;
    color: var(--white);
    font-weight: 700;
    font-size: 18px;
    line-height: 21px;
  }
  .label__origin {
    position: absolute;
    left: 46px; top: 928px;
    display: flex;
    align-items: center;
    gap: 6px;
  }
  .label__origin-text {
    color: var(--flag-red);
    font-weight: 600;
    font-size: 15px;
    line-height: 15px;
    border-left: 2px solid var(--white);
    padding-left: 6px;
  }
  .label__volume {
    position: absolute;
    right: 48px; top: 934px;
    color: var(--white);
    font-weight: 700;
    font-size: 19px;
  }
</style>
</head>
<body>

  <div class="brand-lockup">
    <div class="brand-lockup__name">Brightwell Essence</div>
    <div class="brand-lockup__rule"></div>
  </div>

  <section class="label" aria-label="Spray bottle label">
    <div class="label__photo" role="img" aria-label="Photo of a happy golden retriever on a soft blue fur backdrop"></div>

    <svg class="label__banner" viewBox="0 0 188 106" aria-hidden="true">
      <polygon points="0,0 188,0 188,80 94,106 0,80" fill="#ffffff"/>
    </svg>
    <div class="label__banner-name">Brightwell<br>Essence</div>

    <h1 class="label__title">Colloidal<br>Silver</h1>

    <div class="label__pill">NATURAL FIRST AID<br>FOR PETS</div>

    <p class="label__specs">10 PPM - No Preservaties<br>100% Pure - No Additives</p>
    <div class="label__rule"></div>
    <p class="label__claims">Anti microbial, Anti Fungal,<br>Anti Bacterial, Anti Viral<br>Treats burns, Bites, Cuts, Abrasions,<br>Hots Spots</p>

    <div class="label__origin">
      <svg width="64" height="32" viewBox="0 0 64 32" aria-hidden="true">
        <rect x="0" y="0" width="16" height="32" fill="#e0202a"/>
        <rect x="16" y="0" width="32" height="32" fill="#ffffff"/>
        <rect x="48" y="0" width="16" height="32" fill="#e0202a"/>
      </svg>
      <div class="label__origin-text">MADE IN<br>CANADA</div>
    </div>
    <div class="label__volume">8 oz / 250 ml</div>
  </section>

</body>
</html>
```